User Interface design for the Leaf Butler watering device

Hi Designers

I am designing a new pot plant watering device that clips onto the side of a pot plant and squirts water onto the plant when dry.
I need a designer to come up with an easy to use interface.

Objectives: Simple to understand interface for the average user. User should be able to understand the interface without having to read a manual. The 'feel' should be warm and friendly but also clean. The plan is to print this design on top of any buttons or lights which built into the device. (I can create/move/organise buttons and LED lights, so don't let that constrain the design)

The user interface should have the following options that the user can select:

A. Sensor selection:
1. Semi-wet soil
2. Semi-Dry Soil
3. Wet Soil.
4. Maintain current moisture level

B. Manual override:
1. Water for 5 seconds (small),
2. Water for 10 seconds (medium)
3. Water for 20 seconds (large)
AND
1. Watering frequency 1 day,
2. Watering Frequency 3 days.
3. Watering frequency 7 days.

C. Start/Stop button

Looking forward to your interpretations and designs!
ps: I've already had two logos designed which are provided below and should be incorporated.

Target Market(s)

Home user. Simple to use. Smart home device.

Requirements
Must have
• It should incorporate one of the previous logo designs.

```html
<!DOCTYPE html>
<html lang="en">
<head>
<meta charset="utf-8">
<title>Leaf Butler – Watering Device Interface</title>
<link rel="stylesheet" href="https://fonts.googleapis.com/css2?family=Nunito+Sans:wght@300;400;600;700&display=swap">
<style>
  :root{
    --stage-left-top:#d9dadc;
    --stage-left-bottom:#ebecee;
    --stage-right:#f7f8fa;
    --card:#ffffff;
    --card-head:#f6f6f7;
    --divider:#ececee;
    --ink:#222428;
    --ink-soft:#4a4d53;
    --label:#55585e;
    --icon-grey:#6f747c;
    --icon-blue:#2f9be6;
    --leaf-green:#8cc63f;
    --leaf-green-dark:#76b22e;
    --showcase-grey:#a3a7ad;
    --showcase-blue:#93cff8;
    --tile-border:#dfe1e5;
    --grid-line:#e6e9ee;
  }
  *{box-sizing:border-box;margin:0;padding:0}
  html,body{width:1200px;height:845px;overflow:hidden}
  body{font-family:"Nunito Sans",Arial,sans-serif;position:relative;background:var(--stage-right)}

  .stage-left{position:absolute;left:0;top:0;width:700px;height:845px;
    background:linear-gradient(180deg,var(--stage-left-top),var(--stage-left-bottom))}
  .stage-right{position:absolute;left:700px;top:0;width:500px;height:845px;background:var(--stage-right)}

  /* device panel */
  .panel{position:absolute;left:117px;top:98px;width:466px;height:648px;background:var(--card);
    border-radius:5px;box-shadow:0 1px 3px rgba(0,0,0,.06);overflow:hidden}
  .panel-head{position:absolute;left:0;top:0;width:100%;height:151px;
    background:linear-gradient(180deg,#fff,var(--card-head));border-bottom:1px solid var(--divider)}
  .brand{position:absolute;left:23px;top:86px;font-size:35px;font-weight:700;color:var(--ink);letter-spacing:-.3px;line-height:1}
  .btn-round{position:absolute;border-radius:50%;background:linear-gradient(180deg,#fff,#f1f1f2);
    box-shadow:0 2px 4px rgba(0,0,0,.28),inset 0 0 0 1px #e4e4e6;display:flex;align-items:center;justify-content:center}
  .btn-pause{left:303px;top:56px;width:47px;height:47px}
  .btn-play{left:366px;top:42px;width:74px;height:74px;box-shadow:0 3px 6px rgba(0,0,0,.3),inset 0 0 0 1px #e4e4e6}

  .section{position:absolute;left:0;width:100%;height:165px;border-bottom:1px solid var(--divider);
    background:linear-gradient(180deg,#fff,#fafafa)}
  .section:last-child{border-bottom:none}
  .sec-sensor{top:151px}
  .sec-frequency{top:316px}
  .sec-duration{top:481px;height:167px}
  .section-title{position:absolute;left:25px;top:22px;font-size:17px;font-weight:300;color:var(--ink-soft);letter-spacing:.3px}

  .option{position:absolute;top:56px;width:68px;height:68px;border-radius:50%;
    background:linear-gradient(180deg,#fff,#f5f5f6);box-shadow:inset 0 0 0 1px #ececee;
    display:flex;align-items:center;justify-content:center}
  .option svg{width:42px;height:42px}
  .o1{left:25px}.o2{left:102px}.o3{left:180px}.o4{left:258px}
  .option-label{position:absolute;top:134px;width:90px;text-align:center;font-size:11.5px;color:var(--label);letter-spacing:.4px}
  .l1{left:14px}.l2{left:91px}.l3{left:169px}.l4{left:247px}

  .unit-rule{position:absolute;left:25px;top:143px;width:263px;height:14px;display:flex;align-items:center;gap:12px}
  .unit-rule::before,.unit-rule::after{content:"";flex:1;height:1px;background:#dcdde0}
  .unit-rule span{font-size:12px;letter-spacing:2px;color:var(--label)}

  .btn-cycle{position:absolute;left:379px;top:59px;width:61px;height:61px;border-radius:50%;
    background:linear-gradient(180deg,#fff,#f4f6f1);border:2px solid var(--leaf-green);
    box-shadow:0 2px 4px rgba(0,0,0,.22);display:flex;align-items:center;justify-content:center}
  .btn-cycle svg{width:38px;height:38px;--ic-main:var(--leaf-green-dark)}

  /* showcase */
  .grid-tile{position:absolute;top:105px;width:163px;height:163px;border:1px solid var(--tile-border);
    background-color:#fbfcfd;
    background-image:linear-gradient(var(--grid-line) 1px,transparent 1px),linear-gradient(90deg,var(--grid-line) 1px,transparent 1px);
    background-size:6.8px 6.8px}
  .grid-tile svg{width:100%;height:100%;--ic-main:var(--showcase-blue);--ic-accent:var(--showcase-blue)}
  .gt1{left:742px}.gt2{left:945px}

  .mini{position:absolute;width:51px;height:50px;border:1px solid var(--tile-border);background:#f9fafb;
    display:flex;align-items:center;justify-content:center}
  .mini svg{width:40px;height:40px;--ic-main:var(--showcase-grey);--ic-accent:var(--showcase-grey)}
  .c1{left:742px}.c2{left:810px}.c3{left:877px}.c4{left:945px}.c5{left:1012px}
  .r1{top:304px}.r2{top:372px}.r3{top:439px}

  .showcase-title{position:absolute;left:741px;top:546px;font-size:17px;font-weight:700;color:var(--ink)}
  .showcase-copy{position:absolute;left:741px;top:584px;width:380px;font-size:14px;line-height:18.5px;font-weight:400;color:#6a6d73}

  .ic{fill:none;stroke:var(--ic-main,var(--icon-grey));stroke-width:1.3;stroke-linecap:round;stroke-linejoin:round}
  .ic-accent{fill:none;stroke:var(--ic-accent,var(--icon-blue));stroke-width:1.3;stroke-linecap:round;stroke-linejoin:round}
  .ic-num{fill:var(--ic-main,var(--ink));font-family:"Nunito Sans",Arial,sans-serif;font-weight:600;text-anchor:middle;stroke:none}
  .hidden-defs{position:absolute;width:0;height:0;overflow:hidden}
</style>
</head>
<body>

<svg class="hidden-defs" aria-hidden="true">
  <defs>
    <symbol id="drop-shape" viewBox="0 0 24 24">
      <path d="M12 3.5C10 6.5 7.5 9.8 7.5 13.8a4.5 4.5 0 0 0 9 0C16.5 9.8 14 6.5 12 3.5z"/>
      <path d="M14 14.3a2 2 0 0 1-1.7 1.8"/>
    </symbol>
    <symbol id="icon-drop" viewBox="0 0 24 24">
      <g class="ic-accent"><use href="#drop-shape"/></g>
    </symbol>
    <symbol id="icon-drops-two" viewBox="0 0 24 24">
      <g class="ic"><use href="#drop-shape" x="-5" y="-3" width="16" height="16"/></g>
      <g class="ic-accent"><use href="#drop-shape" x="5" y="2" width="20" height="20"/></g>
    </symbol>
    <symbol id="icon-drops-three" viewBox="0 0 24 24">
      <g class="ic"><use href="#drop-shape" x="-4" y="-3" width="15" height="15"/></g>
      <g class="ic"><use href="#drop-shape" x="13" y="-3" width="15" height="15"/></g>
      <g class="ic-accent"><use href="#drop-shape" x="2" y="3" width="20" height="20"/></g>
    </symbol>
    <symbol id="icon-maintain" viewBox="0 0 24 24">
      <g class="ic">
        <path d="M4.3 15.5A8.5 8.5 0 0 1 18.7 6.6"/>
        <path d="M19.7 8.6A8.5 8.5 0 0 1 5.3 17.4"/>
        <path d="M19.7 5.2v3.4h-3"/>
        <path d="M4.3 18.8v-3.4h3"/>
      </g>
      <g class="ic-accent"><use href="#drop-shape" x="5.5" y="4.5" width="13" height="13"/></g>
    </symbol>
    <symbol id="icon-repeat" viewBox="0 0 24 24">
      <g class="ic">
        <path d="M4 11.5V9.5a2.5 2.5 0 0 1 2.5-2.5H19"/>
        <path d="M16 4l3 3-3 3"/>
        <path d="M20 12.5v2a2.5 2.5 0 0 1-2.5 2.5H5"/>
        <path d="M8 14l-3 3 3 3"/>
      </g>
    </symbol>
    <symbol id="icon-day-ring" viewBox="0 0 24 24">
      <g class="ic">
        <path d="M16.2 6.3A7.5 7.5 0 1 0 11.4 19"/>
        <path d="M16.6 3.5v3.3"/>
      </g>
      <g class="ic-accent"><use href="#drop-shape" x="11" y="9" width="13" height="13"/></g>
    </symbol>
    <symbol id="icon-timer-ring" viewBox="0 0 24 24">
      <g class="ic">
        <circle cx="12" cy="14" r="7.2"/>
        <path d="M9 3.5h6v1.8H9z"/>
        <path d="M12 5.3v1.5"/>
        <path d="M17.2 8.6l1.6-1.6"/>
        <path d="M18 5.8l1.6 1.6"/>
      </g>
    </symbol>
  </defs>
</svg>

<div class="stage-left"></div>
<div class="stage-right"></div>

<main class="panel">
  <header class="panel-head">
    <div class="brand">Leaf Butler</div>
    <div class="btn-round btn-pause" aria-label="Pause">
      <svg width="16" height="16" viewBox="0 0 16 16"><rect x="3" y="2" width="3.2" height="12" rx="1" fill="#6a6d73"/><rect x="9.8" y="2" width="3.2" height="12" rx="1" fill="#6a6d73"/></svg>
    </div>
    <div class="btn-round btn-play" aria-label="Start">
      <svg width="30" height="30" viewBox="0 0 30 30"><path d="M8 3L27 15 8 27z" fill="var(--leaf-green)"/></svg>
    </div>
  </header>

  <section class="section sec-sensor">
    <h2 class="section-title">SENSOR SELECTION</h2>
    <div class="option o1"><svg viewBox="0 0 24 24"><use href="#icon-drop"/></svg></div>
    <div class="option o2"><svg viewBox="0 0 24 24"><use href="#icon-drops-two"/></svg></div>
    <div class="option o3"><svg viewBox="0 0 24 24"><use href="#icon-drops-three"/></svg></div>
    <div class="option o4"><svg viewBox="0 0 24 24"><use href="#icon-maintain"/></svg></div>
    <div class="option-label l1">Semi-Dry</div>
    <div class="option-label l2">Semi-Wet</div>
    <div class="option-label l3">Wet</div>
    <div class="option-label l4">Maintain</div>
    <div class="btn-cycle"><svg viewBox="0 0 24 24"><use href="#icon-repeat"/></svg></div>
  </section>

  <section class="section sec-frequency">
    <h2 class="section-title">WATERING FREQUENCY</h2>
    <div class="option o1"><svg viewBox="0 0 24 24"><use href="#icon-day-ring"/><text class="ic-num" x="9.6" y="15.4" font-size="9.5">1</text></svg></div>
    <div class="option o2"><svg viewBox="0 0 24 24"><use href="#icon-day-ring"/><text class="ic-num" x="9.6" y="15.4" font-size="9.5">3</text></svg></div>
    <div class="option o3"><svg viewBox="0 0 24 24"><use href="#icon-day-ring"/><text class="ic-num" x="9.6" y="15.4" font-size="9.5">7</text></svg></div>
    <div class="unit-rule"><span>DAYS</span></div>
    <div class="btn-cycle"><svg viewBox="0 0 24 24"><use href="#icon-repeat"/></svg></div>
  </section>

  <section class="section sec-duration">
    <h2 class="section-title">WATER FOR</h2>
    <div class="option o1"><svg viewBox="0 0 24 24"><use href="#icon-timer-ring"/><text class="ic-num" x="12" y="17.2" font-size="8.5">5</text></svg></div>
    <div class="option o2"><svg viewBox="0 0 24 24"><use href="#icon-timer-ring"/><text class="ic-num" x="12" y="17.2" font-size="8.5">10</text></svg></div>
    <div class="option o3"><svg viewBox="0 0 24 24"><use href="#icon-timer-ring"/><text class="ic-num" x="12" y="17.2" font-size="8.5">20</text></svg></div>
    <div class="unit-rule"><span>SECONDS</span></div>
    <div class="btn-cycle"><svg viewBox="0 0 24 24"><use href="#icon-repeat"/></svg></div>
  </section>
</main>

<aside>
  <div class="grid-tile gt1"><svg viewBox="0 0 24 24" style="--ic-main:var(--showcase-blue)"><g style="stroke-width:.6"><use href="#icon-maintain" style="stroke-width:.6"/></g></svg></div>
  <div class="grid-tile gt2"><svg viewBox="0 0 24 24"><use href="#icon-timer-ring"/><text class="ic-num" x="12" y="17.4" font-size="8.5" style="font-weight:700">5</text></svg></div>

  <div class="mini c1 r1"><svg viewBox="0 0 24 24"><use href="#icon-drop"/></svg></div>
  <div class="mini c2 r1"><svg viewBox="0 0 24 24"><use href="#icon-drops-two"/></svg></div>
  <div class="mini c3 r1"><svg viewBox="0 0 24 24"><use href="#icon-drops-three"/></svg></div>
  <div class="mini c4 r1"><svg viewBox="0 0 24 24"><use href="#icon-maintain"/></svg></div>
  <div class="mini c5 r1"><svg viewBox="0 0 24 24"><use href="#icon-repeat"/></svg></div>

  <div class="mini c1 r2"><svg viewBox="0 0 24 24"><use href="#icon-day-ring"/><text class="ic-num" x="9.6" y="15.4" font-size="9.5">1</text></svg></div>
  <div class="mini c2 r2"><svg viewBox="0 0 24 24"><use href="#icon-day-ring"/><text class="ic-num" x="9.6" y="15.4" font-size="9.5">3</text></svg></div>
  <div class="mini c3 r2"><svg viewBox="0 0 24 24"><use href="#icon-day-ring"/><text class="ic-num" x="9.6" y="15.4" font-size="9.5">7</text></svg></div>

  <div class="mini c1 r3"><svg viewBox="0 0 24 24"><use href="#icon-timer-ring"/><text class="ic-num" x="12" y="17.2" font-size="8.5">5</text></svg></div>
  <div class="mini c2 r3"><svg viewBox="0 0 24 24"><use href="#icon-timer-ring"/><text class="ic-num" x="12" y="17.2" font-size="8.5">10</text></svg></div>
  <div class="mini c3 r3"><svg viewBox="0 0 24 24"><use href="#icon-timer-ring"/><text class="ic-num" x="12" y="17.2" font-size="8.5">20</text></svg></div>

  <h3 class="showcase-title">All icons designed with pixel perfect quality</h3>
  <p class="showcase-copy">High quality pixel perfect icons designed to look crisp and detailed even at small sizes. All icons are designed on a precise 24px grid system.</p>
</aside>

</body>
</html>
```